Pest Control - Brolga Pest Management

Pest Control
Termites (white ants)
Cockroaches
Ants
Spiders
Bed Bugs
Rats & Mice
Bird Proofing
Termite Inspections
Termite Baiting
Pest Identification

Commercial Services
Integrated Pest Management
Scheduled Servicing
Stored Product Pest
Rodent & Bird Control

Pre - Construction
Physical Termite Barriers
Chemical Barrier Installation
Reticulation Termite Barriers

Industry/Entity Type

Construction

Contact Information for Business Card

Malcolm: 0412 738 261
Tess: 0419 582 047

```html
<!DOCTYPE html>
<html lang="en">
<head>
<meta charset="utf-8">
<title>Brolga Pest Management – Business Card</title>
<link rel="stylesheet" href="https://fonts.googleapis.com/css2?family=Arimo:wght@400;700&display=swap">
<style>
  :root {
    --backdrop: #1c1c1d;
    --card: #e4e4e4;
    --red: #e8232a;
    --navy: #173a5e;
    --ink: #1f2f45;
  }
  * { margin: 0; padding: 0; box-sizing: border-box; }
  html, body {
    width: 1200px; height: 800px; overflow: hidden;
    background: var(--backdrop);
    font-family: "Arimo", Arial, sans-serif;
  }
  .stage { position: relative; width: 1200px; height: 800px; }
  .card {
    position: absolute; top: 247px;
    width: 480px; height: 290px;
    background: var(--card);
    box-shadow: 0 6px 18px rgba(0,0,0,.45);
  }
  .card--front { left: 99px; }
  .card--back { left: 622px; }

  .brand {
    position: absolute; left: 0; right: 0; top: 98px;
    display: flex; align-items: center; justify-content: center; gap: 12px;
  }
  .brand__mark { width: 20px; height: 20px; background: var(--red); }
  .brand__name {
    font-weight: 700; font-size: 30px; color: var(--navy);
    letter-spacing: -0.5px;
  }

  .pest-list {
    position: absolute; left: 0; right: 0; top: 227px;
    text-align: center; font-size: 10.5px; line-height: 14.5px; color: var(--ink);
  }
  .sep { color: var(--red); margin: 0 4px; }

  .services {
    position: absolute; left: 0; right: 0; top: 31px;
    text-align: center; color: var(--ink);
  }
  .services__heading {
    display: inline-block; color: var(--red);
    font-size: 10.5px; letter-spacing: .2px;
    border-bottom: 1px solid var(--red);
    padding: 0 2px 1px; margin-bottom: 4px;
  }
  .services__list { list-style: none; font-size: 10.5px; }
  .services__list li { position: relative; height: 18.5px; line-height: 13px; }
  .services__list li + li::before {
    content: "x"; position: absolute; left: 0; right: 0; top: -9px;
    color: var(--red); font-size: 9.5px; line-height: 9px;
  }
  .services__group + .services__group { margin-top: 2px; }

  .contacts {
    position: absolute; left: 0; right: 0; top: 244px;
    text-align: center; font-weight: 700; font-size: 15px; color: var(--navy);
    letter-spacing: .2px; word-spacing: 1px;
  }
  .contacts__name { color: var(--red); }
  .contacts__gap { display: inline-block; width: 14px; }
</style>
</head>
<body>
<main class="stage">
  <section class="card card--front">
    <div class="brand">
      <span class="brand__mark"></span>
      <span class="brand__name">Brolga Pest Management</span>
    </div>
    <p class="pest-list">
      Termites (white ants)<span class="sep">x</span>Cockroaches<span class="sep">x</span>Ants<span class="sep">x</span>Spiders<span class="sep">x</span>Bed Bugs<span class="sep">x</span>Rats &amp; Mice<br>
      Bird Proofing<span class="sep">x</span>Termite Inspections<span class="sep">x</span>Termite Baiting<span class="sep">x</span>Pest Identification
    </p>
  </section>

  <section class="card card--back">
    <div class="services">
      <div class="services__group">
        <h2 class="services__heading">COMMERCIAL SERVICES</h2>
        <ul class="services__list">
          <li>Integrated Pest Management</li>
          <li>Scheduled Servicing</li>
          <li>Stored Product Pest</li>
          <li>Rodent &amp; Bird Control</li>
        </ul>
      </div>
      <div class="services__group">
        <h2 class="services__heading">PRE - CONSTRUCTION</h2>
        <ul class="services__list">
          <li>Physical Termite Barriers</li>
          <li>Chemical Barrier Installation</li>
          <li>Reticulation Termite Barriers</li>
          <li>Pest Identification</li>
        </ul>
      </div>
    </div>
    <p class="contacts">
      <span class="contacts__name">MALCOLM:</span> 0412 738 261<span class="contacts__gap"></span><span class="contacts__name">TESS:</span> 0419 582 047
    </p>
  </section>
</main>
</body>
</html>
```